Stylish Design With Simple UI For Appointment Site

ONE WEEK TO GO - STILL CONSIDERING NEW DESIGNS!

Note: Logo file now attached. Extra credit to anyone who offers basic HTML templates in the final deliverable, incorporating the individual components of the design (using DIVs and CSS).

There are two key requirements for this site:

1. It makes our site look like one of the most professional of its kind. We want to look the part;
2. It has a very simple, straight-forward user interface. We're nothing without being intuitive.

Our site will be used by other businesses to set up their own online booking systems.

Logo samples attached. The colour scheme is not yet set but two possible options are:

1. Dark (#323B3A) & Blue (#12B5D4) on White background
2. White & Yellow (#FEF102) on Grey (#3A3A3C) background

For inspiration, and an idea of what we like, take a look at quillpost.example - it's very clear and eye-catching, although its pages are longer than we would like ours to be. Oh but we don't need a chimp! Instead of the section with the chimp in, we would like a changing image headline section on the home page, in the style of bellvarine.example.co.uk (with a less high image; we have attached one image which you may want to try out with this, but happy to see other ideas).

Any graphics included must be royalty free and free for commercial use. Fonts should be readily available and specified.

We would like to see the design applied to the following pages:

1. The main public home page (features header, login prompt, menu, changing image banner with headlines, main body, footer menu).
2. A secondary public page (features a similar layout to home page but without image headline banner, includes extra panels/body detail).
3. The Control Panel page (features several list panels and an add appointment button).
4. A list-style administration page (with popup item editor window).
5. A settings administration page (with form).

In that order, a sample walk-through design spec will be attached.

To summarise, we are looking for someone to put forward not only a design but something which also focuses on the user interface. The designer should consider all of the examples and guidance given, but shouldn't let that limit any innovation.

Happy to respond to any questions and give constant feedback.

Thank you.

-*-*-*-*-*-*-*-*-*-*-*-*-*-*-*-*-

Update, 18th Nov 2011:

1. I'm about the upload the logos so you can incorporate these into your designs.

2. A UI question of mine is how to move from a list view (e.g. Resources) to editing one of those items in the list. In the spec document I showed a popup editor for these items but I don't know if that's the best thing to do. Happy to see other ideas on this - whatever the best user experience would be.

3. On the designs in the spec document I've not included any help functionality. It would be good to include pieces of guidance on each page of the administration area to help the user - guess these could either be info panels on the pages themselves or info popups. Again, would be good to see some ideas in the designs.

Also, just to be clear, I am really looking for something that looks like a modern innovative "web app" rather than it looking like a promotional corporate web site.

Target Market(s)

Owners of businesses of all types (e.g. salons, small hotels, surgeries, etc).

Industry/Entity Type

Commercial

Requirements
Must have
• Headline image transition panel on home page.

Layout, graphic and font styles along similar lines to quillpost.example, bellvarine.example.co.uk, etc.
Nice to have
• Blog feed panel on the home page.

Innovative ideas for improvements to the spec.
Should not have
• Anything which can't be practically rendered when the design is converted to HTML.

Should not be overly influenced by the layout and style in the attached spec - that should just be a guide to the content and layout of the site.

```html
<!DOCTYPE html>
<html lang="en">
<head>
<meta charset="utf-8">
<title>Slotwell – Online Booking</title>
<link rel="stylesheet" href="https://fonts.googleapis.com/css2?family=Open+Sans:wght@400;600;700&family=PT+Sans:wght@400;700&display=swap">
<style>
  :root {
    --dark: #323b3a;
    --blue: #12b5d4;
    --blue-deep: #0b89a6;
    --nav-active: #0a4f60;
    --text: #222;
    --muted: #8a8f8e;
    --line: #dfe3e4;
    --page: #ffffff;
    --footer-link: #8e9594;
  }
  * { box-sizing: border-box; margin: 0; padding: 0; }
  html, body { width: 1200px; height: 951px; overflow: hidden; }
  body {
    position: relative;
    background: linear-gradient(#f2f9fb 0, #ffffff 130px);
    font-family: "Open Sans", Tahoma, sans-serif;
    color: var(--text);
  }

  /* Header */
  .brand { position: absolute; left: 74px; top: 52px; display: flex; align-items: center; gap: 12px; }
  .brand-mark { width: 34px; height: 34px; background: var(--blue); }
  .brand-name { font-size: 30px; font-weight: 600; letter-spacing: 3px; color: var(--dark); }

  .login { position: absolute; left: 534px; top: 67px; }
  .login-label { font-size: 12px; font-weight: 700; color: var(--text); margin-bottom: 7px; font-family: "Open Sans", sans-serif; }
  .login-row { display: flex; align-items: center; }
  .field {
    width: 145px; height: 29px; border: 1px solid #d6dadb; border-radius: 4px;
    background: #fff; font-size: 11px; color: #b4b9ba; padding: 6px 10px; margin-right: 7px;
  }
  .btn-login {
    width: 65px; height: 29px; margin-left: 4px; border-radius: 4px;
    background: linear-gradient(#1fc0dd, var(--blue-deep)); color: #fff;
    font-size: 13px; text-align: center; line-height: 29px;
  }
  .sep { width: 1px; height: 24px; background: var(--line); margin: 0 22px 0 17px; }
  .locale { display: flex; align-items: center; font-size: 12px; color: var(--text); }
  .flag { width: 22px; height: 15px; background: #2c4a8a; margin-right: 7px; }
  .locale-arrow { margin-left: 10px; }

  /* Navigation */
  .main-nav {
    position: absolute; left: 70px; top: 137px; width: 1061px; height: 53px;
    background: linear-gradient(#22c2df, #0fa3c2); border-radius: 5px 5px 0 0; overflow: hidden;
  }
  .main-nav a {
    position: absolute; top: 0; height: 53px; line-height: 53px; transform: translateX(-50%);
    color: #fff; font-family: "PT Sans", sans-serif; font-weight: 700; font-size: 14px; text-decoration: none;
  }
  .main-nav .active {
    left: 0; width: 190px; transform: none; text-align: center;
    background: linear-gradient(#0e6b80, var(--nav-active));
  }

  /* Hero */
  .hero { position: absolute; left: 70px; top: 190px; width: 1061px; height: 346px; border-radius: 0 0 5px 5px; overflow: hidden; }
  .hero-photo {
    position: absolute; inset: 0;
    background: linear-gradient(100deg, #ffffff 0%, #efe6e2 25%, #e8cfc2 45%, #d9b7a6 60%, #eeeeee 80%, #ffffff 100%);
  }
  .hero-photo::after {
    content: ""; position: absolute; left: 0; bottom: 0; width: 560px; height: 120px;
    background: linear-gradient(90deg, rgba(40,28,30,.55), rgba(120,40,70,.35), rgba(255,255,255,0));
  }
  .hero-card {
    position: absolute; left: 639px; top: 70px; width: 368px; height: 215px;
    background: rgba(60,66,66,.88); border-radius: 5px; padding: 22px 31px; color: #fff;
  }
  .hero-title { font-family: "PT Sans", sans-serif; font-weight: 700; font-size: 25px; line-height: 30px; }
  .hero-title em { font-style: normal; color: var(--blue); }
  .hero-text { font-size: 11.5px; line-height: 14.5px; margin-top: 9px; width: 290px; }
  .btn-signup {
    display: block; margin-top: 20px; width: 137px; height: 40px; border-radius: 3px;
    background: linear-gradient(#1ba9c6, #0b7f9b); color: #fff;
    font-family: "PT Sans", sans-serif; font-size: 21px; text-align: center; line-height: 40px;
  }
  .hero-dots { position: absolute; left: 759px; top: 309px; display: flex; gap: 22px; }
  .hero-dots span { width: 11px; height: 11px; border-radius: 50%; background: #3d3735; }
  .hero-dots .on { background: var(--blue-deep); }

  /* Content */
  .section-title { font-size: 19px; color: var(--blue-deep); font-weight: 400; }
  .intro { position: absolute; left: 71px; top: 555px; width: 650px; }
  .intro p { margin-top: 10px; font-size: 13.4px; line-height: 16.5px; }
  .benefits { list-style: none; margin-top: 30px; }
  .benefits li { font-size: 13.4px; line-height: 22px; padding-left: 15px; position: relative; }
  .benefits li::before {
    content: ""; position: absolute; left: 0; top: 8px;
    border-left: 6px solid var(--blue); border-top: 3.5px solid transparent; border-bottom: 3.5px solid transparent;
  }
  .divider { position: absolute; left: 767px; top: 541px; width: 14px; height: 272px;
    background: linear-gradient(90deg, rgba(0,0,0,.06), rgba(0,0,0,0)); }

  .news { position: absolute; left: 797px; top: 555px; width: 336px; }
  .news-item { margin-left: 1px; padding: 14px 0 12px; font-size: 13.2px; line-height: 15px; }
  .news-item + .news-item { border-top: 1px dotted #bfc5c6; padding-top: 12px; }
  .news-item h3 { font-size: 14px; font-weight: 700; color: #333; }
  .view-more { display: inline-block; margin-left: 1px; margin-top: 14px; font-size: 11.5px; color: var(--blue-deep); text-decoration: underline; }

  /* Footer */
  .site-footer { position: absolute; left: 0; top: 831px; width: 1200px; height: 120px; background: var(--dark); }
  .footer-nav { position: absolute; left: 72px; top: 34px; display: flex; align-items: center; font-size: 13.4px; }
  .footer-nav a { color: var(--footer-link); text-decoration: none; }
  .footer-nav a.current { color: #fff; }
  .footer-nav i { width: 4px; height: 4px; border-radius: 50%; background: #5b6463; margin: 0 12px; }
  .copyright { position: absolute; left: 72px; top: 60px; font-size: 11.5px; color: #7b8382; }
  .follow { position: absolute; left: 894px; top: 35px; display: flex; align-items: center; }
  .follow-label { color: #fff; font-weight: 700; font-size: 13.4px; margin-right: 27px; }
  .social { width: 38px; height: 38px; border-radius: 50%; background: #434c4b; margin-right: 12px; }
</style>
</head>
<body>
  <header>
    <div class="brand"><span class="brand-mark"></span><span class="brand-name">SLOTWELL</span></div>
    <form class="login">
      <div class="login-label">Login</div>
      <div class="login-row">
        <div class="field">Username</div>
        <div class="field">Password</div>
        <div class="btn-login">Login</div>
        <div class="sep"></div>
        <div class="locale">
          <span class="flag"></span>United State - English
          <svg class="locale-arrow" width="12" height="12" viewBox="0 0 12 12"><circle cx="6" cy="6" r="6" fill="#12b5d4"/><path d="M3.5 4.8 6 7.6 8.5 4.8z" fill="#fff"/></svg>
        </div>
      </div>
    </form>
  </header>

  <nav class="main-nav">
    <a class="active" href="#">HOME</a>
    <a href="#" style="left:307px">FEATURES</a>
    <a href="#" style="left:512px">PRICING</a>
    <a href="#" style="left:729px">SERVICES</a>
    <a href="#" style="left:918px">CONTACT US</a>
  </nav>

  <section class="hero">
    <div class="hero-photo" role="img" aria-label="Relaxing spa massage scene with pink gerbera flowers"></div>
    <div class="hero-card">
      <h2 class="hero-title">Save <em>50%</em> for Massage<br>Booking on August</h2>
      <p class="hero-text">Ut wisi enim ad minim veniam, quis nostrud exerci tation ullamcorper suscipit lobortis nisl ut aliquip ex ea commodo consequat.</p>
      <span class="btn-signup">Sign up</span>
    </div>
    <div class="hero-dots"><span class="on"></span><span></span><span></span><span></span></div>
  </section>

  <main>
    <section class="intro">
      <h2 class="section-title">Make your self available</h2>
      <p>Lorem ipsum dolor sit amet, consectetuer adipiscing elit, sed diam nonummy nibh euismod tincidunt ut laoreet dolore magna aliquam erat volutpat. Ut wisi enim ad minim veniam, quis nostrud exerci tation ullamcorper suscipit lobortis nisl ut aliquip ex ea commodo consequat.</p>
      <ul class="benefits">
        <li>Lorem ipsum dolor sit amet, consectetuer adipiscing elit.</li>
        <li>Accumsan et iusto odio dignissim qui blandit</li>
        <li>Ut wisi enim ad minim veniam</li>
        <li>Vulputate velit esse molestie consequat</li>
      </ul>
    </section>
    <div class="divider"></div>
    <aside class="news">
      <h2 class="section-title">What’s Happening ?</h2>
      <div class="news-item">
        <h3>Save 50% or more with Flash Deals</h3>
        <p>Lorem ipsum dolor sit amet, consectetuer adipiscing elit, sed diam nonummy nibh.</p>
      </div>
      <div class="news-item">
        <h3>Booking on your smartphone</h3>
        <p>ulputate velit esse molestie consequat, vel illum dolore eu</p>
      </div>
      <a class="view-more" href="#">View more</a>
    </aside>
  </main>

  <footer class="site-footer">
    <nav class="footer-nav">
      <a class="current" href="#">Home</a><i></i>
      <a href="#">Work</a><i></i>
      <a href="#">Blog</a><i></i>
      <a href="#">Products</a><i></i>
      <a href="#">Services</a><i></i>
      <a href="#">Support</a><i></i>
      <a href="#">About</a><i></i>
      <a href="#">Contact us</a>
    </nav>
    <p class="copyright">Copyright © 2011 Slotwell. All right reserved.</p>
    <div class="follow">
      <span class="follow-label">Follow Us</span>
      <span class="social"></span><span class="social"></span><span class="social"></span>
    </div>
  </footer>
</body>
</html>
```